bluecastle aquatics of northeast florida business card

I need a new attractive business card. I am planning on printing on very thick rounded corner stock and having painted edges. We are a swimming pool remodel, repair, and service company in north florida. Our current logo is red, white, and blue. It doesn't necessarily have to stay that way, I am open to other ideas. It will need to contain my name, work and cell numbers, email, website, and my contractor license number.

Target Market(s)

High end residential and commercial clients

Industry/Entity Type

Business

Contact Information for Business Card

Company name, employee name and title, work and cell phone numbers, email and website, and Contractor number.

our work scope should be on card somewhere: remodel ~ repair ~ service

logo or slight variation of logo also. (not necessarily set on keeping exact logo)

Colors

Designer to choose colors to be used in the design.

Requirements
Nice to have
• We deal with water so I think some sort of water element or just a color similar to pool water would be nice to integrate into design.

```html
<!DOCTYPE html>
<html lang="en">
<head>
<meta charset="utf-8">
<title>Bluecastle Aquatics of Northeast Florida – Business Card</title>
<link rel="stylesheet" href="https://fonts.googleapis.com/css2?family=Montserrat:wght@300;400;600;700&display=swap">
<style>
  :root {
    --page-bg: #e4e5e7;
    --brand-blue: #0a78cf;
    --deep-blue: #0766b8;
    --water-light: #e6f6fb;
    --water-mid: #bfe6f3;
    --accent-red: #e8262b;
    --frame-cyan: #34d3f0;
    --white: #ffffff;
  }
  * { margin: 0; padding: 0; box-sizing: border-box; }
  html, body {
    width: 1200px; height: 800px; overflow: hidden;
    background: var(--page-bg);
    font-family: "Montserrat", Arial, sans-serif;
  }
  .sheet {
    width: 1200px; height: 800px;
    display: flex; align-items: center; justify-content: center; gap: 40px;
  }
  .card {
    position: relative; width: 560px; height: 320px;
    border-radius: 14px; overflow: hidden;
    box-shadow: 0 6px 18px rgba(0,0,0,.12);
  }

  /* Back */
  .card-back { background: var(--brand-blue); }
  .card-back .backdrop {
    position: absolute; inset: 0;
    background: radial-gradient(ellipse at 30% 30%, #1d8ee0 0%, var(--brand-blue) 55%, var(--deep-blue) 100%);
  }
  .logo-plate {
    position: absolute; left: 50%; top: 112px; transform: translateX(-50%);
    height: 66px; background: var(--white);
    outline: 2px solid var(--frame-cyan); outline-offset: 4px;
    display: flex; align-items: center; gap: 12px; padding: 0 22px;
    white-space: nowrap;
  }
  .logo-dot {
    width: 30px; height: 30px; border-radius: 50%;
    background: var(--accent-red); flex: none;
  }
  .logo-name {
    color: var(--brand-blue); font-weight: 600; text-transform: uppercase;
    letter-spacing: 2px; line-height: 1.25; white-space: nowrap;
  }
  .logo-name .main { display: block; font-size: 15px; }
  .logo-name .sub { display: block; font-size: 9px; letter-spacing: 2.5px; }
  .license {
    position: absolute; left: 0; right: 0; top: 204px; text-align: center;
    color: var(--white); font-weight: 600; font-size: 14px; letter-spacing: .5px;
  }
  .scope {
    position: absolute; left: 0; right: 0; top: 232px; text-align: center;
    color: var(--white); font-weight: 400; font-size: 11px; letter-spacing: 2.5px;
    text-transform: uppercase;
  }

  /* Front */
  .card-front .water {
    position: absolute; inset: 0;
    background: linear-gradient(135deg, var(--water-light) 0%, var(--water-mid) 50%, var(--water-light) 100%);
  }
  .card-front .panel { position: absolute; inset: 0; }
  .front-logo {
    position: absolute; left: 24px; top: 52px;
    display: flex; align-items: center; gap: 8px;
  }
  .front-logo .logo-dot { width: 22px; height: 22px; }
  .front-logo .logo-name { letter-spacing: 1.5px; }
  .front-logo .logo-name .main { font-size: 12px; }
  .front-logo .logo-name .sub { font-size: 7.5px; letter-spacing: 1.8px; }
  .details {
    position: absolute; right: 28px; top: 30px; width: 280px;
    color: var(--white); text-align: right;
  }
  .person-name { font-size: 26px; letter-spacing: .5px; text-transform: uppercase; white-space: nowrap; }
  .person-name .first { font-weight: 700; }
  .person-name .last { font-weight: 300; }
  .person-title { font-size: 11px; letter-spacing: 1px; text-transform: uppercase; margin-top: 2px; }
  .address { font-size: 12.5px; line-height: 1.4; margin-top: 22px; }
  .contacts { list-style: none; margin-top: 24px; font-size: 12.5px; line-height: 1.6; }
  .contacts li { display: flex; justify-content: flex-end; align-items: center; gap: 7px; white-space: nowrap; }
  .contacts .label { font-weight: 600; }
  .contacts svg { width: 12px; height: 12px; fill: var(--white); flex: none; }
</style>
</head>
<body>
<main class="sheet">

  <section class="card card-back" aria-label="Card back">
    <div class="backdrop" role="img" aria-label="Faint photo of a pool ladder in blue water"></div>
    <div class="logo-plate">
      <span class="logo-dot"></span>
      <span class="logo-name"><span class="main">Bluecastle Aquatics</span><span class="sub">of Northeast Florida</span></span>
    </div>
    <p class="license">Lic No: #CPC5518207</p>
    <p class="scope">Remodel ~ Repair ~ Service</p>
  </section>

  <section class="card card-front" aria-label="Card front">
    <div class="water" role="img" aria-label="Light rippling pool water texture"></div>
    <svg class="panel" viewBox="0 0 560 320" aria-hidden="true">
      <path d="M340 0 C250 60 215 220 250 320 L560 320 L560 0 Z" fill="var(--brand-blue)"/>
      <path d="M340 0 C250 60 215 220 250 320" fill="none" stroke="var(--accent-red)" stroke-width="4"/>
    </svg>
    <div class="front-logo">
      <span class="logo-dot"></span>
      <span class="logo-name"><span class="main">Bluecastle Aquatics</span><span class="sub">of Northeast Florida</span></span>
    </div>
    <div class="details">
      <h1 class="person-name"><span class="first">Daniel</span> <span class="last">Reyes</span></h1>
      <p class="person-title">Managing Director</p>
      <p class="address">Harbor Point Plaza, Suite 4,<br>48 Marsh Lane, Florida</p>
      <ul class="contacts">
        <li><span><span class="label">W</span> 904-555-0148</span>
          <svg viewBox="0 0 24 24"><path d="M6.6 10.8a15 15 0 0 0 6.6 6.6l2.2-2.2c.3-.3.7-.4 1-.2 1.1.4 2.3.6 3.6.6.6 0 1 .4 1 1V20c0 .6-.4 1-1 1A17 17 0 0 1 3 4c0-.6.4-1 1-1h3.5c.6 0 1 .4 1 1 0 1.3.2 2.5.6 3.6.1.3 0 .7-.2 1z"/></svg></li>
        <li><span><span class="label">C</span> 904-555-0193</span>
          <svg viewBox="0 0 24 24"><path d="M7 2h10a2 2 0 0 1 2 2v16a2 2 0 0 1-2 2H7a2 2 0 0 1-2-2V4a2 2 0 0 1 2-2zm0 3v12h10V5zm5 13.2a1.2 1.2 0 1 0 0 2.4 1.2 1.2 0 0 0 0-2.4z" fill-rule="evenodd"/></svg></li>
        <li>daniel@bluecastleaquatics.com
          <svg viewBox="0 0 24 24"><path d="M2 5h20v14H2z M4 7v.5l8 5 8-5V7l-8 5z" fill-rule="evenodd"/></svg></li>
        <li>www.bluecastleaquatics.com
          <svg viewBox="0 0 24 24"><path d="M12 2a10 10 0 1 0 0 20 10 10 0 0 0 0-20zm6.9 6h-3a15 15 0 0 0-1.3-3.9A8 8 0 0 1 18.9 8zM12 4c.8 1.2 1.5 2.5 1.9 4h-3.8c.4-1.5 1.1-2.8 1.9-4zM4.3 14a8 8 0 0 1 0-4h3.4a16 16 0 0 0 0 4zm.8 2h3a15 15 0 0 0 1.3 3.9A8 8 0 0 1 5.1 16zm3-8h-3a8 8 0 0 1 4.3-3.9A15 15 0 0 0 8.1 8zM12 20c-.8-1.2-1.5-2.5-1.9-4h3.8c-.4 1.5-1.1 2.8-1.9 4zm2.3-6H9.7a14 14 0 0 1 0-4h4.6a14 14 0 0 1 0 4zm.3 5.9a15 15 0 0 0 1.3-3.9h3a8 8 0 0 1-4.3 3.9zM16.3 14a16 16 0 0 0 0-4h3.4a8 8 0 0 1 0 4z"/></svg></li>
      </ul>
    </div>
  </section>

</main>
</body>
</html>
```